Webdesign for a Bikeshop in Innsbruck (male audience)

To obtain my master's degree, I am conducting a study in the field of web design as part of my master thesis. All submitted designs will therefore be used for study purposes. In order to achieve a homogeneous group, I would like to encourage not only male but also female web designers to submit a design. All submitted designs will be used anonymously for the study and therefore do not allow any conclusions to be drawn about your person. Since this is a contest, the winner will be chosen randomly from all serious submissions. I would be really happy if you would support me in my study. I think the results could be very informative and also useful for your further work (I won't go into more detail here as it could skew the results - but once the contest is over, feel free to contact me. Of course I will also provide you with my results as soon as my work is finished). Below you will find a fictitious usecase and a description of what the website should include:

The company Brenvik Outfitters is planning to relaunch its own website and would like to present itself primarily as a competent and leading consultant in the field of cargo bikes. The design should appeal to a broad audience and embody an urban lifestyle. In any case, the website should include a landing page, a product overview page and a product details page. The company also wants to appeal mainly to a MALE target group. You only design the website. So don't worry about hardware or software limitations, just create the best bike store design you can.

As it is fictitious, I can't offer any materials. A logo is not necessary, you can use a placeholder or whatever you have access to. If you need any inspring websites feel free to contact me.

Target Market(s)

male users

Number of Pages Required

1 page

Requirements
Must have
• landing page, product overview page, product details page
Should not have
• online shop

```html
<!DOCTYPE html>
<html lang="en">
<head>
<meta charset="utf-8">
<title>Brenvik Outfitters</title>
<link href="https://fonts.googleapis.com/css2?family=Montserrat:wght@500;600;700&family=Roboto:wght@400;500;700&display=swap" rel="stylesheet">
<style>
:root{
  --navy:#053566;
  --navy-dark:#032a52;
  --orange:#ec9f3c;
  --cream:#fcf0de;
  --ink:#1b1b1b;
  --muted:#555;
  --line:#dcdcdc;
  --white:#fff;
}
*{margin:0;padding:0;box-sizing:border-box}
html,body{width:1200px;height:4338px;overflow:hidden}
body{position:relative;background:var(--white);font-family:'Roboto',sans-serif;color:var(--ink)}
.abs{position:absolute}
a{color:inherit;text-decoration:none}

/* header */
.topbar{left:269px;top:0;width:660px;height:42px;background:var(--navy);border-radius:0 0 40px 40px;color:#fff;font-size:14px;display:flex;align-items:center;justify-content:center;gap:34px}
.topbar span{display:flex;align-items:center;gap:10px}
.topbar .phone{font-weight:700;font-size:17px}
.logo{left:110px;top:28px;font-family:'Montserrat',sans-serif;font-weight:700;font-size:26px;line-height:30px;color:var(--navy)}
.nav{left:340px;top:63px;display:flex;gap:36px;font-size:14px;font-weight:500}
.nav .active{color:var(--orange)}
.btn{display:inline-flex;align-items:center;justify-content:center;gap:10px;background:var(--orange);color:#fff;border-radius:30px;font-size:13px;font-weight:700;text-transform:uppercase}
.shop{left:939px;top:52px;width:148px;height:42px}

/* hero */
.hero{left:0;top:103px;width:1200px;height:558px;background:linear-gradient(90deg,#6c6252 0%,#5a4f40 40%,#2d2a26 70%,#1a1a1a 100%)}
.hero-copy{left:607px;top:250px;color:#fff}
.hero-copy .pre{font-family:'Montserrat',sans-serif;font-weight:600;font-size:26px}
.hero-copy h1{font-family:'Montserrat',sans-serif;font-weight:600;font-size:50px;margin-top:8px;letter-spacing:.5px}
.hero-copy p{font-size:17px;line-height:26px;width:490px;margin-top:14px}
.hero-btn{left:607px;top:464px;width:148px;height:42px}
.dots{left:1132px;top:332px;display:flex;flex-direction:column;gap:12px}
.dots i{width:10px;height:10px;border-radius:50%;background:#fff;display:block}
.dots i.on{background:transparent;border:2px solid #fff}

/* who */
.h2{font-family:'Montserrat',sans-serif;font-weight:700;font-size:27px;color:var(--ink);text-transform:uppercase}
.who-title{left:111px;top:786px}
.who-text{left:111px;top:836px;width:452px;font-size:14px;line-height:24.8px;color:var(--muted);text-align:justify}
.who-btn{left:111px;top:1084px;width:148px;height:40px}
.who-ring{left:640px;top:731px;width:456px;height:456px;border-radius:50%;background:#f6dcb4;box-shadow:0 0 24px rgba(0,0,0,.12)}
.who-photo{left:656px;top:747px;width:424px;height:424px;border-radius:50%;background:linear-gradient(160deg,#7b4a3a 0%,#5e5650 45%,#8d8d88 75%,#b0aca4 100%);border:8px solid #fff}

/* products */
.band{left:0;top:1286px;width:1200px;height:382px;background:var(--navy)}
.center-title{width:1200px;left:0;text-align:center}
.prod-title{top:1348px;color:#fff}
.card{background:#fff;box-shadow:0 2px 10px rgba(0,0,0,.15)}
.prod{top:1437px;width:316px;height:391px}
.prod .img{position:absolute;left:8px;top:8px;right:8px;height:214px;background:linear-gradient(180deg,#f2f3f4,#e7e9eb)}
.prod h3{position:absolute;top:246px;width:100%;text-align:center;font-size:21px;font-weight:500}
.prod .rule{position:absolute;top:285px;left:50%;margin-left:-18px;width:36px;height:2px;background:var(--navy)}
.prod p{position:absolute;top:306px;left:18px;right:18px;font-size:14px;line-height:21px;color:var(--muted);text-align:justify;text-align-last:center}
.arrow{top:1853px;width:37px;height:35px;border:1px solid #ccc;background:#fff;display:flex;align-items:center;justify-content:center}

/* why */
.why-title{top:1962px}
.why{left:116px;top:2041px;width:968px;height:192px;border:1px solid var(--line)}
.why-item{top:2041px;width:242px;height:192px;display:flex;flex-direction:column;align-items:center;justify-content:center;gap:20px;font-size:16px;font-weight:500;text-align:center;border-right:1px solid var(--line)}
.why-item.active{background:var(--navy);color:#fff;top:2033px;height:208px;box-shadow:0 6px 18px rgba(0,0,0,.2);border:none}
.why-bar{left:627px;width:188px;height:8px;background:var(--orange)}

/* gallery */
.gallery{left:0;top:2353px;width:1200px;height:749px;background:var(--cream)}
.gal-title{top:2422px}
.ph{position:absolute}
.gal-btn{left:507px;top:2982px;width:185px;height:47px}

/* blog */
.blog-title{top:3186px}
.blog{top:3267px;width:316px;height:399px;border-radius:14px;border:6px solid #f3f3f3;box-shadow:0 2px 10px rgba(0,0,0,.1);overflow:hidden}
.blog .img{height:196px}
.blog .meta{height:52px;display:flex;align-items:center;gap:18px;padding-left:22px;font-size:13px;color:#444;border-bottom:1px solid #eee}
.blog h4{font-size:16px;font-weight:700;line-height:24px;padding:16px 22px 0}
.blog p{font-size:13px;line-height:20px;color:#666;padding:10px 22px 0}
.blog.hot{background:var(--orange);border-color:#f3c586}
.blog.hot .meta,.blog.hot h4,.blog.hot p{color:#fff;border-color:rgba(255,255,255,.3)}

/* footer */
.footer{left:0;top:3790px;width:1200px;height:498px;background:var(--navy)}
.sub-title{left:111px;top:3863px;font-family:'Montserrat',sans-serif;font-weight:700;font-size:26px;color:#fff}
.sub-text{left:111px;top:3906px;font-size:15px;color:#fff}
.field{left:562px;top:3873px;width:525px;height:49px;background:#fff;display:flex;align-items:center;padding-left:20px;gap:12px;font-size:14px;color:#555}
.field .go{position:absolute;right:0;top:0;width:171px;height:49px;background:var(--orange);color:#fff;font-weight:700;font-size:13px;display:flex;align-items:center;justify-content:center}
.hr{left:111px;top:3965px;width:978px;height:1px;background:rgba(255,255,255,.3)}
.vr{top:4011px;width:1px;height:250px;background:rgba(255,255,255,.3)}
.f-logo{left:111px;top:4026px;font-family:'Montserrat',sans-serif;font-weight:700;font-size:26px;line-height:30px;color:#fff}
.f-text{left:111px;top:4107px;width:400px;font-size:14px;line-height:24px;color:#fff}
.f-h{font-size:16px;font-weight:500;color:#fff}
.f-h::after{content:"";display:block;width:34px;height:2px;background:var(--orange);margin-top:10px}
.links{left:581px;top:4002px}
.links ul{list-style:none;margin-top:22px}
.links li{font-size:13.5px;color:#fff;height:26.8px;display:flex;align-items:center;gap:14px}
.links li::before{content:"+";color:var(--orange);font-weight:700}
.contact{left:793px;top:4002px}
.c-row{display:flex;gap:20px;align-items:center;margin-top:22px;color:#fff}
.c-row small{display:block;color:var(--orange);font-size:12.5px;font-weight:500}
.c-row b{font-size:18px}
.c-row span{font-size:14px}
.bottom{left:0;top:4288px;width:1200px;height:50px;background:var(--orange);color:#fff;font-size:14px;display:flex;align-items:center;justify-content:center}
</style>
</head>
<body>

<header>
  <div class="abs topbar">
    <span><svg width="12" height="16" viewBox="0 0 12 16"><path d="M6 0a6 6 0 0 0-6 6c0 4 6 10 6 10s6-6 6-10a6 6 0 0 0-6-6zm0 8.5A2.5 2.5 0 1 1 6 3.5a2.5 2.5 0 0 1 0 5z" fill="#fff"/></svg>45 , Lorem Ipsum Dolor Sit , USA</span>
    <span>|</span>
    <span class="phone"><svg width="15" height="15" viewBox="0 0 24 24"><path d="M6.6 10.8a15 15 0 0 0 6.6 6.6l2.2-2.2c.3-.3.7-.4 1-.2 1.1.4 2.3.6 3.6.6.6 0 1 .4 1 1V20c0 .6-.4 1-1 1A17 17 0 0 1 3 4c0-.6.4-1 1-1h3.5c.6 0 1 .4 1 1 0 1.3.2 2.5.6 3.6.1.3 0 .7-.2 1z" fill="#fff"/></svg>+ 1 555 014 2290</span>
  </div>
  <div class="abs logo">Brenvik<br>Outfitters</div>
  <nav class="abs nav">
    <a class="active">Home</a><a>About</a><a>Our Products</a><a>Reviews</a><a>Why Choose Us</a><a>Contact</a>
  </nav>
  <a class="abs btn shop">Shop Now <svg width="14" height="13" viewBox="0 0 24 22"><path d="M0 1h4l3 12h13l3-9H6" fill="none" stroke="#fff" stroke-width="2.5"/><circle cx="9" cy="19" r="2" fill="#fff"/><circle cx="19" cy="19" r="2" fill="#fff"/></svg></a>
</header>

<section>
  <div class="abs hero" role="img" aria-label="Courier riding a yellow cargo bike loaded with parcels through a city street"></div>
  <div class="abs hero-copy">
    <div class="pre">Welcome to</div>
    <h1>Brenvik Outfitters</h1>
    <p>Lorem ipsum dolor sit amet, consectetur adipiscing elit, sed do eiusmod tempor incididunt ut labore et dolore</p>
  </div>
  <a class="abs btn hero-btn">Get Started <svg width="14" height="14" viewBox="0 0 16 16"><circle cx="8" cy="8" r="8" fill="#fff"/><path d="M6 4l4 4-4 4" stroke="#ec9f3c" stroke-width="2" fill="none"/></svg></a>
  <div class="abs dots"><i></i><i></i><i class="on"></i><i></i><i></i></div>
</section>

<section>
  <h2 class="abs h2 who-title">Who We Are</h2>
  <p class="abs who-text">Sed ut perspiciatis unde omnis iste natus error sit voluptatem accusantium doloremque laudantium, totam rem aperiam, eaque ipsa quae ab illo inventore veritatis et quasi architecto beatae vitae dicta sunt explicabo. Nemo enim ipsam voluptatem quia voluptas sit aspernatur aut odit aut fugit, sed quia consequuntur magni dolores eos qui ratione voluptatem sequi nesciunt. Neque porro quisquam est, qui dolorem ipsum quia dolor sit amet, consectetur, adipisci velit, sed quia non numquam eius modi tempora incidunt ut labore et dolore magnam aliquam quaerat voluptatem.</p>
  <a class="abs btn who-btn">Get Started <svg width="14" height="14" viewBox="0 0 16 16"><circle cx="8" cy="8" r="8" fill="#fff"/><path d="M6 4l4 4-4 4" stroke="#ec9f3c" stroke-width="2" fill="none"/></svg></a>
  <div class="abs who-ring"></div>
  <div class="abs who-photo" role="img" aria-label="Orange box cargo bike parked in front of a brick building"></div>
  <svg class="abs" style="left:656px;top:747px" width="424" height="424" viewBox="0 0 424 424"><path d="M80 380A200 200 0 0 1 330 50" fill="none" stroke="#053566" stroke-width="6" opacity=".8"/></svg>
</section>

<section>
  <div class="abs band"></div>
  <h2 class="abs h2 center-title prod-title">Our Products</h2>
  <div class="abs card prod" style="left:106px"><div class="img" role="img" aria-label="Cargo bike with orange wooden box"></div><h3>Product Title</h3><div class="rule"></div><p>Lorem ipsum dolor sit amet, consectetur adipiscing elit, sed do eiusmod tempor incididunt ut labore et dolore</p></div>
  <div class="abs card prod" style="left:443px"><div class="img" role="img" aria-label="Black cargo bike with olive front box"></div><h3>Product Title</h3><div class="rule"></div><p>Lorem ipsum dolor sit amet, consectetur adipiscing elit, sed do eiusmod tempor incididunt ut labore et dolore</p></div>
  <div class="abs card prod" style="left:778px"><div class="img" role="img" aria-label="Cream cargo bike with olive front box"></div><h3>Product Title</h3><div class="rule"></div><p>Lorem ipsum dolor sit amet, consectetur adipiscing elit, sed do eiusmod tempor incididunt ut labore et dolore</p></div>
  <div class="abs arrow" style="left:559px"><svg width="18" height="10" viewBox="0 0 18 10"><path d="M18 5H2M6 1L2 5l4 4" stroke="#111" stroke-width="2" fill="none"/></svg></div>
  <div class="abs arrow" style="left:603px"><svg width="18" height="10" viewBox="0 0 18 10"><path d="M0 5h16M12 1l4 4-4 4" stroke="#111" stroke-width="2" fill="none"/></svg></div>
</section>

<section>
  <h2 class="abs h2 center-title why-title">Why Choose Us</h2>
  <div class="abs why"></div>
  <div class="abs why-item" style="left:116px">
    <svg width="98" height="60" viewBox="0 0 98 60"><rect x="0" y="6" width="20" height="5" fill="#053566"/><rect x="4" y="18" width="16" height="5" fill="#053566"/><rect x="0" y="30" width="20" height="5" fill="#053566"/><rect x="14" y="2" width="50" height="40" rx="3" fill="#053566"/><path d="M66 12h16l14 16v14H66z" fill="#053566"/><path d="M72 17h9l8 10H72z" fill="#fff"/><circle cx="32" cy="46" r="9" fill="#053566" stroke="#fff" stroke-width="3"/><circle cx="80" cy="46" r="9" fill="#053566" stroke="#fff" stroke-width="3"/></svg>
    <span>Fully Assembled<br>Shipping</span>
  </div>
  <div class="abs why-item" style="left:358px">
    <svg width="72" height="72" viewBox="0 0 72 72"><circle cx="36" cy="36" r="34" fill="#053566"/><circle cx="36" cy="36" r="29" fill="none" stroke="#fff" stroke-width="1.5" stroke-dasharray="3 3"/><text x="36" y="35" text-anchor="middle" font-family="Montserrat,sans-serif" font-weight="700" font-size="14" fill="#fff">FREE</text><text x="36" y="50" text-anchor="middle" font-family="Montserrat,sans-serif" font-weight="700" font-size="14" fill="#fff">TRIAL</text></svg>
    <span>14-Day Free Trial</span>
  </div>
  <div class="abs why-bar" style="top:2033px"></div>
  <div class="abs why-item active" style="left:600px">
    <svg width="76" height="76" viewBox="0 0 76 76"><ellipse cx="24" cy="14" rx="20" ry="7" fill="#fff"/><rect x="4" y="14" width="40" height="30" fill="#fff"/><path d="M4 24c0 4 9 7 20 7s20-3 20-7M4 34c0 4 9 7 20 7s20-3 20-7" stroke="#053566" stroke-width="2" fill="none"/><circle cx="50" cy="50" r="22" fill="#fff"/><text x="50" y="60" text-anchor="middle" font-family="Roboto,sans-serif" font-weight="700" font-size="28" fill="#053566">$</text></svg>
    <span>Financing Available</span>
  </div>
  <div class="abs why-bar" style="top:2233px"></div>
  <div class="abs why-item" style="left:842px;border-right:none">
    <svg width="76" height="76" viewBox="0 0 76 76"><circle cx="38" cy="12" r="9" fill="#053566"/><path d="M24 40c0-10 6-16 14-16s14 6 14 16z" fill="#053566"/><path d="M4 40l14 28 6-4-6-10h24c6 0 12-4 16-10l10-12-5-4-12 12H34" fill="none" stroke="#053566" stroke-width="6" stroke-linejoin="round"/></svg>
    <span>Service that WOWs</span>
  </div>
</section>

<section>
  <div class="abs gallery"></div>
  <h2 class="abs h2 center-title gal-title">Our Gallery</h2>
  <div class="ph" style="left:111px;top:2501px;width:237px;height:168px;background:linear-gradient(135deg,#1f5573,#3c3f44)" role="img" aria-label="Black cargo bike by a blue door"></div>
  <div class="ph" style="left:111px;top:2681px;width:237px;height:266px;background:linear-gradient(160deg,#7a3a25,#a28d7a 70%,#c9c3b9)" role="img" aria-label="Trike cargo bike in front of a wooden door"></div>
  <div class="ph" style="left:358px;top:2501px;width:238px;height:266px;background:linear-gradient(160deg,#5f8d3c,#9c9a6a 55%,#6b6b62)" role="img" aria-label="Rider on cargo bike carrying boxes in a park"></div>
  <div class="ph" style="left:358px;top:2777px;width:238px;height:170px;background:linear-gradient(90deg,#cbbfa8,#4f7fa5 60%,#6d6a8f)" role="img" aria-label="Black cargo trike beside a graffiti wall"></div>
  <div class="ph" style="left:604px;top:2501px;width:237px;height:168px;background:linear-gradient(180deg,#5d7b3a,#6c6c66 60%,#9b9b96)" role="img" aria-label="Courier on cargo bike crossing a street"></div>
  <div class="ph" style="left:604px;top:2681px;width:237px;height:266px;background:linear-gradient(160deg,#c8ccd0,#8a8d8c 50%,#3a3a3c)" role="img" aria-label="Father riding cargo bike with children in the box"></div>
  <div class="ph" style="left:852px;top:2501px;width:237px;height:266px;background:linear-gradient(180deg,#9fb7c9,#4f7a3a 45%,#6a6c66)" role="img" aria-label="Man riding a blue cargo bike on a park path"></div>
  <div class="ph" style="left:852px;top:2777px;width:237px;height:170px;background:linear-gradient(160deg,#8a8a68,#d9d6cf 50%,#9c2f30)" role="img" aria-label="White cargo bike parked by a bench and flowers"></div>
  <a class="abs btn gal-btn">View All Gallery <svg width="14" height="14" viewBox="0 0 16 16"><circle cx="8" cy="8" r="8" fill="#fff"/><path d="M6 4l4 4-4 4" stroke="#ec9f3c" stroke-width="2" fill="none"/></svg></a>
</section>

<section>
  <h2 class="abs h2 center-title blog-title">Latest <span style="color:var(--navy)">Blog</span></h2>
  <article class="abs card blog" style="left:106px">
    <div class="img" style="background:linear-gradient(160deg,#8fa3b0,#6d7d6a 50%,#c9a27a)" role="img" aria-label="Smiling rider beside a cargo bike with parcels"></div>
    <div class="meta"><span>▦&nbsp; June 2022</span><span>|</span><span>● John Doe</span></div>
    <h4>Lorem ipsum dolor sit amet consectetur</h4>
    <p>Sed ut perspiciatis unde omnis iste natus error sit voluptatem accusantium</p>
  </article>
  <article class="abs card blog hot" style="left:443px">
    <div class="img" style="background:linear-gradient(180deg,#7a4a3a,#c54a22 55%,#6f6f6c)" role="img" aria-label="Orange cargo bike parked on a cobbled street"></div>
    <div class="meta"><span>▦&nbsp; June 2022</span><span>|</span><span>● John Doe</span></div>
    <h4>Lorem ipsum dolor sit amet consectetur</h4>
    <p>Sed ut perspiciatis unde omnis iste natus error sit voluptatem accusantium</p>
  </article>
  <article class="abs card blog" style="left:778px">
    <div class="img" style="background:linear-gradient(180deg,#2d5a9a,#7fa0c8 45%,#c8b43a 70%,#5a7a2a)" role="img" aria-label="Black cargo bike in a field under blue sky"></div>
    <div class="meta"><span>▦&nbsp; June 2022</span><span>|</span><span>● John Doe</span></div>
    <h4>Lorem ipsum dolor sit amet consectetur</h4>
    <p>Sed ut perspiciatis unde omnis iste natus error sit voluptatem accusantium</p>
  </article>
</section>

<footer>
  <div class="abs footer"></div>
  <h3 class="abs sub-title">Subscribe Our Newsletter</h3>
  <p class="abs sub-text">Lorem ipsum dolor sit amet, consectetur adipiscing elit</p>
  <div class="abs field"><svg width="16" height="12" viewBox="0 0 16 12"><rect width="16" height="12" rx="1" fill="#053566"/><path d="M0 1l8 6 8-6" stroke="#fff" stroke-width="1.3" fill="none"/></svg>Enter Your Email<div class="go">SUBSCRIBE NOW</div></div>
  <div class="abs hr"></div>
  <div class="abs vr" style="left:532px"></div>
  <div class="abs vr" style="left:746px"></div>
  <div class="abs f-logo">Brenvik<br>Outfitters</div>
  <p class="abs f-text">Sed ut perspiciatis unde omnis iste natus errorvoluptatem accusantium doloremque laudantium, totam remaperiam, eaque ipsa quae ab illo inventore veritatis</p>
  <div class="abs links">
    <div class="f-h">Quick Links</div>
    <ul><li>Home</li><li>About</li><li>Our Products</li><li>Reviews</li><li>Why Choose Us</li><li>Blog</li><li>Contact</li></ul>
  </div>
  <div class="abs contact">
    <div class="f-h">Contact Us</div>
    <div class="c-row"><svg width="16" height="26" viewBox="0 0 16 26"><rect x="1" y="1" width="14" height="24" rx="2" fill="none" stroke="#fff" stroke-width="2"/><circle cx="8" cy="21" r="1.5" fill="#fff"/></svg><div><small>PHONE NO :</small><b>+ 1 555 014 2290</b></div></div>
    <div class="c-row"><svg width="26" height="18" viewBox="0 0 26 18"><rect x="1" y="1" width="24" height="16" fill="none" stroke="#fff" stroke-width="2"/><path d="M1 1l12 9 12-9M1 17l9-8M25 17l-9-8" stroke="#fff" stroke-width="2" fill="none"/></svg><div><small>E MAIL :</small><span>info@brenvikoutfitters.example</span></div></div>
    <div class="c-row"><svg width="26" height="18" viewBox="0 0 26 18"><rect x="1" y="1" width="24" height="16" fill="none" stroke="#fff" stroke-width="2"/><path d="M1 1l12 9 12-9M1 17l9-8M25 17l-9-8" stroke="#fff" stroke-width="2" fill="none"/></svg><div><small>LOCATION :</small><span>147 , Lorem Ipsum Dolor , United States</span></div></div>
  </div>
  <div class="abs bottom">© 2022 Brenvik Outfitters. All Rights Reserved</div>
</footer>

</body>
</html>
```